BENEATH THE [HARBOR] OF A DAWN, Mend your road

We are looking for a cover refresh of an existing bestselling book that is going into 3rd edition print this year.
The book is an inspirational as well as educational book that has become recognized as one of the most comprehensive, actionable, personal and financial planning resources available today for families, individuals and business owners alike.
Comprised of three true stories of loss, learning to live and love again and a 30 page checklist at the back of the book it contains tips and strategies for everyone to help them to get their personal and financial lives in order while they can.
The cover must have the following:
1. Appeal to a broad audience/both personal and corporate
2. Include Mara Quellton Bestselling Author
3. Include introduction of a new Afterword
4. 3rd Edition
5. Colors to remain the same – red, black and white
6. The title must remain in caps and the word [HARBOR] must have the brackets around it
We have also added a current copy of the second edition to help you. For your information our website is www.thequelltonhouse.example
Reason: We have narrowed it down to our top 3 designs. We are submitting the covers to our community for them to pick the top cover. Good luck to everyone

```html
<!DOCTYPE html>
<html lang="en">
<head>
<meta charset="utf-8">
<title>Beneath the [Harbor] of a Dawn — Mara Quellton</title>
<link rel="stylesheet" href="https://fonts.googleapis.com/css2?family=Bebas+Neue&family=Dancing+Script:wght@500;600&display=swap">
<style>
  :root {
    --cover-red: #e00000;
    --ink-black: #0a0a0a;
    --paper-white: #ffffff;
    --nib-light: #f2f2f2;
    --nib-mid: #d9d9d9;
  }
  html, body {
    margin: 0;
    padding: 0;
    width: 866px;
    height: 1200px;
    overflow: hidden;
    background: var(--paper-white);
  }
  .cover {
    position: relative;
    width: 866px;
    height: 1200px;
    box-sizing: border-box;
    border: 22px solid var(--cover-red);
    background: var(--paper-white);
    font-family: "Bebas Neue", "Arial Narrow", sans-serif;
    color: var(--ink-black);
  }
  .nib-illustration {
    position: absolute;
    left: 0;
    top: 0;
    width: 150px;
    height: 1005px;
    background: linear-gradient(180deg, var(--nib-light) 0%, var(--nib-mid) 100%);
  }
  .book-title { margin: 0; font-weight: 400; }
  .title-line {
    position: absolute;
    left: 190px;
    width: 600px;
    display: flex;
    justify-content: space-between;
    line-height: 1;
  }
  .title-top {
    top: 52px;
    font-size: 134px;
    letter-spacing: 6px;
  }
  .title-band {
    position: absolute;
    left: 160px;
    top: 171px;
    width: 662px;
    height: 185px;
    background: var(--ink-black);
    color: var(--paper-white);
    font-size: 200px;
    line-height: 185px;
    text-align: center;
    letter-spacing: 4px;
  }
  .title-band .accent-letter { color: var(--cover-red); }
  .title-bottom {
    top: 362px;
    font-size: 144px;
    letter-spacing: 18px;
  }
  .afterword-note {
    position: absolute;
    right: 32px;
    top: 494px;
    margin: 0;
    font-family: "Dancing Script", cursive;
    font-weight: 500;
    font-size: 46px;
    color: var(--cover-red);
    line-height: 1;
    white-space: nowrap;
  }
  .edition {
    position: absolute;
    right: 32px;
    top: 574px;
    margin: 0;
    font-size: 72px;
    line-height: 1;
    letter-spacing: 1px;
  }
  .edition sup {
    font-size: 36px;
    vertical-align: 26px;
    margin-right: 6px;
  }
  .author-tag {
    position: absolute;
    right: 32px;
    top: 965px;
    margin: 0;
    font-family: "Dancing Script", cursive;
    font-weight: 600;
    font-size: 62px;
    line-height: 1;
  }
  .author-name {
    position: absolute;
    left: 46px;
    width: 740px;
    top: 1044px;
    margin: 0;
    display: flex;
    justify-content: space-between;
    font-size: 96px;
    line-height: 1;
    font-weight: 400;
  }
  .author-name span { letter-spacing: 14px; }
  .author-name span:last-child { letter-spacing: 14px; margin-right: -14px; }
</style>
</head>
<body>
  <main class="cover">
    <div class="nib-illustration" role="img" aria-label="Line illustration of a fountain pen nib descending the left edge, ending in a flourish under the author line"></div>

    <h1 class="book-title">
      <span class="title-line title-top"><span>BENEATH</span><span>THE</span></span>
      <span class="title-band">[HARB<span class="accent-letter">O</span>R]</span>
      <span class="title-line title-bottom"><span>OF</span><span>A</span><span>DAWN</span></span>
    </h1>

    <p class="afterword-note">Introduction of a new Afterword</p>
    <p class="edition">3<sup>RD</sup>EDITION</p>

    <p class="author-tag">Bestselling Author</p>
    <p class="author-name"><span>MARA</span><span>QUELLTON</span></p>
  </main>
</body>
</html>
```